Pruett Design & Millwork needs a web presence. Looking for a unique Design so please submit an idea.

In brief, you should know the following about me: My company was established in 2001 and had been responsible for providing reasonable CAD Design and Custom Millwork ever since. My specialty is in the area Architectural CAD Design, Fabrication of Custom Millwork and Mouldings on a partime basis. Drawings and estimates done at a very reasonable cost. I look forward to working on your next project. Thanks in Advance, Glen 
I would like one page to show thumbnails linked to some of past millwork projects and another page with thumbnails linking to some of my house designs. I assume last page will have contact information accessed from a link on home page. I already had a logo designed which I can supply you with to design home page around. As I indicated I have a regular full time job and do this for additional income and will move to full time when I have enough business.

I have attached the logo I had designed in a couple different colors. I have also uploaded some PDF's of files that I also considered before choosing the RED LOGO to give an ideas of how we could tweak the logo to better fit the website if need be. Text is wrong in those.

Thanks,
Glen

I added my logo as a PDF side there seems to be a problem with scaling loge with the other file. Hope this helps.

Glen

Evening,
I will be hosting this site on servquill. Its looks like it will get launched with wordpress?  What will be involved from getting your design up so I can upload project pictures and and text to areas you have set aside? I am also going to upload a couple jpg of a couple recent projects so you can put in so I can get a feel of what they will look like. Thanks for all your work to date! Glen

I am not seeing alot of design variations or even many designers in fact. Is there something more from me you need? Do you need me to extend deadline?

Reason: It appears that your need some more time to submit some design changes. I will choose a design next week after changes have been submitted. Thanks for your time. Glen

Reason: Designers needs a couple days to submit some last minute changes. Thanks for all your submissions! Glen

Reason: Some last minute designs that I need to look at and give feedback on. I want to thank everyone for their designs and patience. Thanks again, Glen

Evening All,

Upon discussion with a couple of the designers I want the design done in Word Press and I have increased budget the amount they said they would need to do it for. Thanks for all submissions so far but I am still looking for the special one that stands out among the rest! Glen

I will not be extending deadline and choosing designer tomorrow morning so if you have anything else to add please do so tonight. Thanks for all your submissions. Glen

Target Market(s)

Millwork projects will be generally local where as CAD Design Projects could be emailed anywhere. Probably more USA but who knows.

Industry/Entity Type

House

Font styles to use
Other font styles liked:
• Eras Medium ITC, Calibri or Designers choice.

Requirements
Must have
• Must tie in my logo on Homepage at least. Could even be somewhat transparent in background? I will let the designer work that out.
Nice to have
• Page to point to current and past Design projects on one page and millwork on another.
Should not have
• Target a large Corporate or Global environment since it is a small business right now.

```html
<!DOCTYPE html>
<html lang="en">
<head>
<meta charset="utf-8">
<title>Pruett Design &amp; Millwork</title>
<link rel="stylesheet" href="https://fonts.googleapis.com/css2?family=Roboto:ital,wght@0,300;0,400;0,700;1,400&family=Oswald:wght@400;500&family=Russo+One&family=Great+Vibes&family=Open+Sans:ital,wght@0,400;0,700;1,400&display=swap">
<style>
:root{
  --red:#c4161c;
  --red-dark:#8e0f13;
  --ink:#2a2a2a;
  --text:#444;
  --muted:#8a8a8a;
  --light:#f0f0f0;
  --line:#dcdcdc;
  --dark:#1d1a1a;
  --white:#fff;
  --sky:#3f7fcb;
  --sky-light:#a9cbeb;
  --grass:#3d6a25;
}
*{box-sizing:border-box;margin:0;padding:0}
html,body{width:1200px;height:3392px;overflow:hidden}
body{background:var(--white);font-family:"Open Sans",Arial,sans-serif;color:var(--text);position:relative}
.section{position:absolute;left:0;width:1200px}
.section-title{font-family:"Roboto",Arial,sans-serif;font-weight:300;font-size:42px;text-align:center;color:var(--red)}

/* nav */
.site-nav{position:absolute;top:0;left:0;width:1200px;height:41px;background:rgba(70,70,70,.78);display:flex;justify-content:center;z-index:3}
.site-nav a{font-family:"Roboto",Arial,sans-serif;font-size:15px;color:var(--white);text-decoration:none;line-height:41px;padding:0 24px}
.site-nav a.active{background:var(--red)}

/* hero */
.hero{top:0;height:617px;overflow:hidden;
  background:
    radial-gradient(ellipse 420px 260px at 830px 250px,rgba(255,255,255,.95) 0%,rgba(255,255,255,0) 70%),
    radial-gradient(ellipse 380px 220px at 250px 170px,rgba(255,255,255,.9) 0%,rgba(255,255,255,0) 70%),
    radial-gradient(ellipse 520px 200px at 600px 560px,rgba(190,190,190,.55) 0%,rgba(190,190,190,0) 75%),
    radial-gradient(ellipse 300px 260px at 1120px 120px,rgba(205,205,205,.7) 0%,rgba(205,205,205,0) 75%),
    radial-gradient(ellipse 280px 240px at 60px 420px,rgba(200,200,200,.7) 0%,rgba(200,200,200,0) 75%),
    linear-gradient(180deg,#e2e2e2 0%,#f3f3f3 40%,#ebebeb 75%,#d9d9d9 100%)}
.hero-brand{position:absolute;top:196px;left:0;width:1200px;display:flex;justify-content:center;align-items:center;gap:18px}
.brand-mark{width:64px;height:64px;background:var(--red)}
.brand-name{font-family:"Roboto",Arial,sans-serif;font-weight:700;font-size:42px;color:var(--ink)}
.hero-line{position:absolute;top:360px;width:1200px;text-align:center;font-family:"Oswald",Arial,sans-serif;font-weight:400;font-size:56px;line-height:70px;color:#1e1e1e;transform:scaleX(.86)}
.hero-headline{position:absolute;top:436px;width:1200px;text-align:center;font-family:"Russo One",Arial,sans-serif;font-size:88px;line-height:92px;color:var(--red);letter-spacing:4px}
.scroll-down{position:absolute;left:578px;top:560px;width:44px;height:46px;background:var(--red)}

/* about */
.about{top:625px;height:280px;background:var(--white)}
.about .section-title{margin-top:38px}
.about p{width:930px;margin:14px auto 0;font-size:12.5px;line-height:19px;text-align:center;color:var(--text)}
.about p + p{margin-top:20px}

/* what I do */
.services{top:919px;height:446px;
  background:
    radial-gradient(ellipse 380px 260px at 230px 110px,rgba(230,80,80,.55) 0%,rgba(230,80,80,0) 75%),
    radial-gradient(ellipse 360px 260px at 1040px 330px,rgba(240,150,150,.45) 0%,rgba(240,150,150,0) 75%),
    radial-gradient(ellipse 300px 200px at 760px 80px,rgba(120,10,14,.5) 0%,rgba(120,10,14,0) 75%),
    linear-gradient(135deg,#a3141a 0%,#c8242a 40%,#b51c22 65%,#cf3a3e 100%)}
.services .section-title{color:var(--white);margin-top:52px;font-size:50px}
.services ul{list-style:none;width:900px;margin:18px auto 0}
.services li{font-size:13px;font-weight:700;color:var(--white);text-align:center;line-height:30px;white-space:nowrap;border-bottom:1px dotted rgba(255,255,255,.55);margin:0 60px}
.services li:last-child{border-bottom:0}

/* current projects */
.projects{top:1373px;height:524px;background:var(--white);border-top:8px solid var(--light)}
.projects .section-title{margin-top:46px}
.project-card{position:absolute;top:140px;width:298px}
.project-photo{height:166px}
.card-title{margin-top:20px;font-size:14px;font-weight:700;color:var(--red);padding-bottom:8px;border-bottom:2px solid var(--line)}
.card-text{margin-top:10px;font-size:11.5px;line-height:16px;color:var(--muted)}
.btn-small{display:inline-block;margin-top:12px;padding:4px 12px;font-size:11px;color:#555;background:#e4e4e4;border:1px solid #cfcfcf}

/* testimonials */
.testimonials{top:1904px;height:446px;background:var(--dark)}
.testimonials .section-title{color:var(--white);margin-top:40px;font-size:42px}
.testimonial{position:absolute;top:106px;width:220px;text-align:center}
.portrait{width:136px;height:136px;margin:0 auto;border-radius:50%;border:4px solid var(--white);box-shadow:0 0 0 2px #555;
  background:linear-gradient(180deg,#f4f4f4 0%,#eee 35%,#c9a58a 50%,#b88e72 60%,#2c2f36 72%,#1b1d22 100%)}
.quote-name{margin-top:12px;font-family:"Great Vibes",cursive;font-size:26px;color:var(--white)}
.quote-text{font-size:11.5px;font-weight:700;line-height:15px;color:var(--white)}
.btn-read{display:inline-block;margin-top:14px;padding:2px 14px;background:var(--white);color:#222;font-family:"Great Vibes",cursive;font-size:15px}

/* previous works */
.works{top:2358px;height:476px;background:var(--white);border-top:8px solid var(--light)}
.works .section-title{margin-top:36px}
.works-lead{margin-top:12px;text-align:center;font-size:14px;color:var(--ink)}
.works-sub{text-align:center;font-size:11px;font-style:italic;color:var(--red)}
.slide{position:absolute;top:182px;width:306px;height:190px;overflow:hidden}
.slide-next{position:absolute;right:4px;top:0;width:32px;height:36px;background:#111}
.slide-tag{position:absolute;right:0;bottom:38px;background:var(--red);color:var(--white);font-family:"Oswald",Arial,sans-serif;font-size:19px;padding:1px 12px;transform:scaleX(.9);transform-origin:right}
.slide-caption{position:absolute;right:0;bottom:6px;background:var(--white);color:#222;font-family:"Roboto",Arial,sans-serif;font-style:italic;font-size:19px;padding:2px 12px}
.dots{position:absolute;top:400px;width:1200px;display:flex;justify-content:center;gap:6px}
.dots span{width:11px;height:11px;border-radius:50%;border:1px solid #bbb;background:#f4f4f4}
.dots span.on{background:var(--red);border-color:var(--red)}

/* contact */
.contact{top:2834px;height:526px}
.map{position:absolute;inset:0;
  background:
    radial-gradient(ellipse 260px 200px at 120px 180px,rgba(170,200,140,.6) 0%,rgba(170,200,140,0) 75%),
    radial-gradient(ellipse 240px 200px at 1040px 300px,rgba(175,205,150,.55) 0%,rgba(175,205,150,0) 75%),
    radial-gradient(ellipse 300px 220px at 300px 430px,rgba(200,195,215,.5) 0%,rgba(200,195,215,0) 75%),
    radial-gradient(ellipse 280px 220px at 850px 120px,rgba(215,205,180,.8) 0%,rgba(215,205,180,0) 75%),
    linear-gradient(135deg,#e9e5d8 0%,#ddd8c6 40%,#e7e2d3 70%,#d9d4c2 100%)}
.contact-info{position:absolute;left:464px;top:44px;width:263px;height:150px;background:rgba(40,40,40,.88);color:var(--white);text-align:center;padding-top:14px}
.info-phone{font-size:16px}
.info-mail{font-size:15px;margin-top:4px}
.info-mail i{display:inline-block;width:16px;height:11px;background:var(--red);margin-right:6px;vertical-align:middle}
.info-addr{font-size:12.5px;line-height:16px;margin-top:12px}
.contact-head{position:absolute;left:464px;top:200px;width:263px;height:46px;background:rgba(40,40,40,.92);color:var(--white);font-family:"Roboto",Arial,sans-serif;font-weight:300;font-size:30px;text-align:center;line-height:46px}
.contact-form{position:absolute;left:464px;top:252px;width:263px;height:240px;background:var(--white);padding:12px 10px}
.field{height:36px;border:1px solid var(--line);margin-bottom:10px;font-size:11px;color:#999;padding:8px 10px}
.field.message{height:72px}
.btn-submit{display:block;margin:4px auto 0;width:82px;height:28px;background:var(--red);color:var(--white);font-size:12px;font-weight:700;text-align:center;line-height:28px;border-radius:3px}

/* footer */
.site-footer{top:3360px;height:32px;background:#2b2b2b;color:#888;font-size:10px;line-height:32px;padding-left:110px}
.social{position:absolute;right:100px;top:0;display:flex;gap:3px}
.social span{width:28px;height:32px;background:#1e1e1e}
.social span:first-child{background:var(--red)}
</style>
</head>
<body>

<nav class="site-nav">
  <a class="active" href="#">Home</a>
  <a href="#">Past and Current Projects</a>
  <a href="#">Millwork</a>
  <a href="#">Contact Us</a>
</nav>

<header class="section hero" role="img" aria-label="Architectural blueprints and a white house model">
  <div class="hero-brand">
    <span class="brand-mark"></span>
    <span class="brand-name">Pruett Design &amp; Millwork</span>
  </div>
  <h1 class="hero-line">Lorem ipsum dolor sit amet</h1>
  <p class="hero-headline">DONEC A LECTUS NON</p>
  <a class="scroll-down" href="#" aria-label="Scroll down">
    <svg width="44" height="46" viewBox="0 0 44 46"><path d="M15 19l7 7 7-7" fill="none" stroke="#fff" stroke-width="3"/></svg>
  </a>
</header>

<section class="section about">
  <h2 class="section-title">About Me</h2>
  <p>Lorem ipsum dolor sit amet, consectetur adipiscing elit. Nulla lobortis consequat mauris, eget eleifend nunc viverra viverra. Ut ac risus odio. Aliquam pretium purus sed nulla feugiat blandit. Cras vel libero ut lacus eleifend tempor.</p>
  <p>Phasellus eleifend, magna non tincidunt accumsan, justo arcu cursus ipsum, non porttitor sapien quam vel magna. Maecenas elit nisl, molestie nec dapibus nec, aliquet a erat. Donec scelerisque lacus a libero suscipit auctor volutpat enim euismod. Mauris porta, lacus ut ullamcorper sodales, mauris tortor feugiat purus, nec aliquam neque purus ac metus. Nunc eleifend leo quis nisl hendrerit ultrices. Suspendisse quis feugiat elit. Fusce vitae dolor ac est tincidunt feugiat. Phasellus volutpat dui in sapien malesuada tempus placerat justo ultricies. Duis mollis ornare risus, ut consectetur mi tincidunt sit amet.</p>
</section>

<section class="section services" role="img" aria-label="Red tinted 3D framing model of a house over blueprints">
  <h2 class="section-title">What I Do</h2>
  <ul>
    <li>Lorem ipsum dolor sit amet, consectetur adipiscing elit. Nulla lobortis consequat mauris, eget eleifend nunc viverra viverra.</li>
    <li>Ut ac risus odio. Aliquam pretium purus sed nulla feugiat blandit. Cras vel libero ut lacus eleifend tempor.</li>
    <li>Phasellus eleifend, magna non tincidunt accumsan, justo arcu cursus ipsum, non porttitor sapien quam vel magna.</li>
    <li>Maecenas elit nisl, molestie nec dapibus nec, aliquet a erat. Donec scelerisque lacus a libero suscipit auctor euismod.</li>
    <li>Mauris porta, lacus ut ullamcorper sodales, mauris tortor feugiat purus, nec aliquam neque purus ac metus.</li>
    <li>Nunc eleifend leo quis nisl hendrerit ultrices. Suspendisse quis feugiat elit.</li>
    <li>Fusce vitae dolor ac est tincidunt feugiat. Phasellus volutpat dui in sapien malesuada tempus placerat justo ultricies.</li>
    <li>Duis mollis ornare risus, ut consectetur mi tincidunt sit amet.</li>
  </ul>
</section>

<section class="section projects">
  <h2 class="section-title">Current Projects</h2>
  <article class="project-card" style="left:123px">
    <div class="project-photo" role="img" aria-label="Rendering of a grey two-storey house on a lawn" style="background:linear-gradient(180deg,#3f86d6 0%,#93c0ec 30%,#b8b6ae 45%,#7d7a73 62%,#6e9a3e 76%,#3d6a25 100%)"></div>
    <h3 class="card-title">Consectetur adipiscing elit</h3>
    <p class="card-text">Lorem ipsum dolor sit amet, consectetur adipiscing elit. Nulla lobortis consequat mauris, eget eleifend nunc viverra viverra. Ut ac risus odio. Aliquam pretium purus sed nulla feugiat blandit. Cras vel libero ut.</p>
    <span class="btn-small">View Details</span>
  </article>
  <article class="project-card" style="left:452px">
    <div class="project-photo" role="img" aria-label="Rendering of a yellow house with a dark roof" style="background:linear-gradient(180deg,#3a78c8 0%,#9fc5ea 28%,#4a4644 42%,#c79a34 58%,#a67b22 74%,#2f5d1e 100%)"></div>
    <h3 class="card-title">Consectetur adipiscing elit</h3>
    <p class="card-text">Lorem ipsum dolor sit amet, consectetur adipiscing elit. Nulla lobortis consequat mauris, eget eleifend nunc viverra viverra. Ut ac risus odio. Aliquam pretium purus sed nulla feugiat blandit. Cras vel libero ut.</p>
    <span class="btn-small">View Details</span>
  </article>
  <article class="project-card" style="left:779px">
    <div class="project-photo" role="img" aria-label="Rendering of a brown house with a balcony" style="background:linear-gradient(180deg,#3c7ac6 0%,#a6c8e8 25%,#6a4a34 40%,#4e3626 60%,#8c8c88 78%,#5d5d5a 100%)"></div>
    <h3 class="card-title">Consectetur adipiscing elit</h3>
    <p class="card-text">Lorem ipsum dolor sit amet, consectetur adipiscing elit. Nulla lobortis consequat mauris, eget eleifend nunc viverra viverra. Ut ac risus odio. Aliquam pretium purus sed nulla feugiat blandit. Cras vel libero ut.</p>
    <span class="btn-small">View Details</span>
  </article>
</section>

<section class="section testimonials">
  <h2 class="section-title">Testimonials</h2>
  <figure class="testimonial" style="left:116px">
    <div class="portrait" role="img" aria-label="Client portrait"></div>
    <figcaption>
      <p class="quote-name">Donec a lectus</p>
      <p class="quote-text">Lorem ipsum dolor sit amet, consec adipiscing elit. Nulla lobortis consequat mauris, eget eleifend nuncviverra.</p>
      <span class="btn-read">Read More</span>
    </figcaption>
  </figure>
  <figure class="testimonial" style="left:363px">
    <div class="portrait" role="img" aria-label="Client portrait"></div>
    <figcaption>
      <p class="quote-name">Donec a lectus</p>
      <p class="quote-text">Lorem ipsum dolor sit amet, consec adipiscing elit. Nulla lobortis consequat mauris, eget eleifend nuncviverra.</p>
      <span class="btn-read">Read More</span>
    </figcaption>
  </figure>
  <figure class="testimonial" style="left:612px">
    <div class="portrait" role="img" aria-label="Client portrait"></div>
    <figcaption>
      <p class="quote-name">Donec a lectus</p>
      <p class="quote-text">Lorem ipsum dolor sit amet, consec adipiscing elit. Nulla lobortis consequat mauris, eget eleifend nuncviverra.</p>
      <span class="btn-read">Read More</span>
    </figcaption>
  </figure>
  <figure class="testimonial" style="left:861px">
    <div class="portrait" role="img" aria-label="Client portrait"></div>
    <figcaption>
      <p class="quote-name">Donec a lectus</p>
      <p class="quote-text">Lorem ipsum dolor sit amet, consec adipiscing elit. Nulla lobortis consequat mauris, eget eleifend nuncviverra.</p>
      <span class="btn-read">Read More</span>
    </figcaption>
  </figure>
</section>

<section class="section works">
  <h2 class="section-title">Previous Works</h2>
  <p class="works-lead">Lorem ipsum dolor sit amet, consectetur adipiscing elit. Nulla lobortis consequat mauris, eget eleifend nunc viverra viverra. Ut ac risus odio.</p>
  <p class="works-sub">Aliquam pretium purus sed nulla feugiat blandit. Cras vel libero ut lacus eleifend tempor.</p>
  <div class="slide" style="left:137px;background:linear-gradient(180deg,#2c6cbf 0%,#8db7e3 28%,#8a7c6c 42%,#5e5044 60%,#3b6a24 78%,#24461a 100%)" role="img" aria-label="Rendering of a large house with a deck">
    <span class="slide-next"><svg width="32" height="36" viewBox="0 0 32 36"><path d="M13 11l7 7-7 7" fill="none" stroke="#fff" stroke-width="3"/></svg></span>
    <span class="slide-tag">SAPIEN INTERDUM</span>
    <span class="slide-caption">mauris tortor feugiat</span>
  </div>
  <div class="slide" style="left:447px;background:linear-gradient(180deg,#3874c2 0%,#a0c3e8 28%,#9c8c72 44%,#6e6050 60%,#3f7226 78%,#2a501b 100%)" role="img" aria-label="Rendering of a house with a front porch">
    <span class="slide-next"><svg width="32" height="36" viewBox="0 0 32 36"><path d="M13 11l7 7-7 7" fill="none" stroke="#fff" stroke-width="3"/></svg></span>
    <span class="slide-tag">SAPIEN INTERDUM</span>
    <span class="slide-caption">mauris tortor feugiat</span>
  </div>
  <div class="slide" style="left:757px;background:linear-gradient(180deg,#3c78c4 0%,#a3c4e6 24%,#6a4a34 40%,#4e3626 60%,#8c8c88 80%,#5d5d5a 100%)" role="img" aria-label="Rendering of a brown house with a balcony">
    <span class="slide-next"><svg width="32" height="36" viewBox="0 0 32 36"><path d="M13 11l7 7-7 7" fill="none" stroke="#fff" stroke-width="3"/></svg></span>
    <span class="slide-tag">SAPIEN INTERDUM</span>
    <span class="slide-caption">mauris tortor feugiat</span>
  </div>
  <div class="dots"><span class="on"></span><span></span><span></span><span></span></div>
</section>

<section class="section contact">
  <div class="map" role="img" aria-label="Street map of the local area"></div>
  <div class="contact-info">
    <p class="info-phone">00000000000</p>
    <p class="info-mail"><i></i>info@pruettmillwork.com</p>
    <p class="info-addr">Lorem ipsum dolor,<br>sit amet, consectetur adipiscing<br>amet, consectetur adipi</p>
  </div>
  <h2 class="contact-head">Contact Us</h2>
  <form class="contact-form">
    <div class="field">Name</div>
    <div class="field">Email</div>
    <div class="field message">Message</div>
    <span class="btn-submit">Submit</span>
  </form>
</section>

<footer class="section site-footer">
  © 2014 Pruett Design &amp; Millwork . All Rights Reserved.
  <div class="social"><span></span><span></span><span></span><span></span><span></span></div>
</footer>

</body>
</html>
```